Website for Company to help with House Restoration from Hurricane Damage

Crisp, Clean and Professional!

I need a FRONT page for a website. I need it created in photoshop with the layers intact. We DO NOT need the HTML or RBT for the site. Simply the design. Any fonts you use will need to be included if they are not standard. Please make sure any fonts you use in the body of the text are available for use on Google Fonts.

I have attached a word doc that lists the menu items and additional instructions.

A little about the company - after Hurricane Quintessa - RBT developed a system which allows the house to be raised, the Pylonets installed, and the house reset on the Pylonets without the expense of moving the house or driving new pilings. This option can be installed in a matter of days with limited space and at a lower construction cost.

Please refer to the attached musthaves.doc and images that are included.

The main page must incorporate the menu, the attached photos w/ text underneath (text is in the word doc attached), and the text included in the word doc.

Standard footer with contact info as well.

If you have questions please contact us!
Updates

Designs are due by Friday! We will pick one this weekend.  We are unable to change it from 10 days to 5.  Thank you!!!

Target Market(s)

People who lost their homes or businesses due to a hurricane.

Industry/Entity Type

Construction

Requirements
Must have
• See attached musthaves.doc

```html
<!DOCTYPE html>
<html lang="en">
<head>
<meta charset="utf-8">
<title>Resilient Base Technologies, LLC</title>
<link rel="stylesheet" href="https://fonts.googleapis.com/css2?family=Carlito:wght@400;700&family=Open+Sans:wght@400;600;700&display=swap">
<style>
:root{
  --header-top:#c9d8a6;
  --header-bottom:#7d9250;
  --olive:#7b8c55;
  --sage:#c5d6a0;
  --mist:#eef0e6;
  --stripe:#f1f1ee;
  --ink:#111111;
  --footer:#474a40;
  --footer-text:#e9ecdf;
  --white:#ffffff;
}
*{margin:0;padding:0;box-sizing:border-box}
html,body{width:1148px;height:1200px;overflow:hidden;background:var(--white)}
body{position:relative;font-family:"Carlito",Calibri,sans-serif;color:var(--ink)}
.abs{position:absolute}

.header{left:0;top:0;width:1148px;height:238px;background:linear-gradient(var(--header-top),#a9bf80 55%,var(--header-bottom))}
.top-tab-dark{left:991px;top:0;width:56px;height:8px;background:#111}
.top-tab-olive{left:1047px;top:0;width:57px;height:8px;background:var(--olive)}
.brand-disc{left:42px;top:17px;width:156px;height:156px;border-radius:50%;background:var(--white);box-shadow:0 3px 8px rgba(0,0,0,.35);display:flex;align-items:center;justify-content:center;font-family:"Open Sans",sans-serif;font-weight:700;font-size:40px;color:#3f5321}
.company-name{left:224px;top:80px;font-family:"Open Sans",sans-serif;font-weight:700;font-size:25px;letter-spacing:.2px;color:var(--ink)}
.call-label{right:52px;top:55px;font-family:"Open Sans",sans-serif;font-size:15px;color:var(--ink)}
.call-number{right:52px;top:78px;font-family:"Open Sans",sans-serif;font-size:24px;color:var(--ink)}
.main-nav{left:225px;top:151px;display:flex;gap:27px;font-family:"Open Sans",sans-serif;font-size:15px;color:var(--ink);list-style:none}

.stripe-band{left:0;top:238px;width:1148px;height:313px;background:repeating-linear-gradient(90deg,var(--stripe) 0 3px,#e6e6e2 3px 4px)}
.hero{left:68px;top:195px;width:1019px;height:355px;border:3px solid var(--white);box-shadow:0 0 18px rgba(0,0,0,.45);background:linear-gradient(#a9a6c6 0%,#e0a3a0 22%,#f0bca0 28%,#8f93ad 34%,#606a88 60%,#4a4d5c 82%,#5d5a5c 100%)}
.hero-text{left:100px;top:346px;font-family:"Carlito",sans-serif;font-weight:700;font-size:27px;line-height:36px;color:var(--white)}

.welcome-band{left:0;top:551px;width:1148px;height:52px;background:var(--mist)}
.welcome-title{left:80px;top:563px;font-family:"Carlito",sans-serif;font-size:24px;color:var(--ink)}
.welcome-rule{left:78px;top:600px;width:507px;height:2px;background:var(--olive)}

.intro{left:80px;top:619px;width:677px;font-size:14.4px;line-height:19.5px;text-align:justify}
.intro p{margin-bottom:19px}

.services-head{left:788px;top:605px;width:297px;height:44px;background:var(--sage);padding:10px 0 0 20px;font-size:20px}
.services-photo{left:801px;top:665px;width:268px;height:131px;background:linear-gradient(90deg,#3b4149,#2a2e34 60%,#474c55)}
.services-text{left:801px;top:808px;width:268px;font-size:14.4px;line-height:19px;text-align:justify}
.know-more{left:805px;top:924px;font-size:16px;font-weight:700;color:var(--olive)}

.footer-shape{left:0;top:0}
.footer-col-title{font-size:19px;color:var(--footer-text)}
.footer-rule{height:1px;background:#8d9470}
.quick-links{left:80px;top:1012px;width:144px}
.quick-links ul{list-style:none;margin-top:14px;font-size:14.4px;line-height:19.5px;color:var(--footer-text)}
.testimonials{left:263px;top:1012px;width:296px}
.testimonials blockquote{margin-top:14px;padding-left:4px;font-size:14.4px;line-height:19.5px;color:var(--footer-text)}
.testimonials cite{display:block;font-style:normal;font-weight:700}
.contact{left:674px;top:1012px;width:290px;text-align:right;color:var(--footer-text)}
.contact .org{font-size:19px;margin-top:4px}
.contact address{font-style:normal;font-size:13.5px;line-height:19px}
.copyright-band{left:0;top:1153px;width:1148px;height:47px;background:var(--olive)}
.copyright{left:81px;top:1169px;font-size:12.6px;color:var(--white)}
</style>
</head>
<body>

<header>
  <div class="abs header"></div>
  <div class="abs top-tab-dark"></div>
  <div class="abs top-tab-olive"></div>
  <div class="abs brand-disc">RBT</div>
  <h1 class="abs company-name">RESILIENT BASE TECHNOLOGIES, LLC</h1>
  <div class="abs call-label">CALL US NOW</div>
  <div class="abs call-number">(555) 014 2290</div>
  <ul class="abs main-nav">
    <li>HOME</li><li>SERVICES</li><li>ABOUT US</li><li>PRODUCT SPECIFICATIONS</li><li>DESIGN DOCUMENTATION</li><li>CONTACT USA</li>
  </ul>
</header>

<section>
  <div class="abs stripe-band"></div>
  <div class="abs hero" role="img" aria-label="Photo of a parent and small child on a beach at sunset, boats on the bay behind"></div>
  <p class="abs hero-text">REBUILD SAFER,<br>STRONGER,<br>BETTER TO BUILD NEW<br>LASTING MEMORIES</p>
</section>

<main>
  <div class="abs welcome-band"></div>
  <h2 class="abs welcome-title">Welcome to Resilient Base Technologies</h2>
  <div class="abs welcome-rule"></div>
  <div class="abs intro">
    <p>Systems for extending the height of existing piles are not available on today’s market. Resilient Base Technologies, LLC (RBT) has developed two systems to allow for Piles to be extended that provide superior structural support without corrosion and maintenance concerns. We provided two systems, a complete system, Pile Cap Extension Pylonets, and Pile Splice.</p>
    <p>These two systems allow a home to be raised to by up to 54”, higher extensions possible with additional design consideration for lateral support. Shown below is the full Piling Extension system, which connects to the top of the existing pile. The system modular and can be cut to meet specific needs of the home.</p>
    <p>Our Patented Piling system has been designed to withstand the corrosive environment of beach communities. The salt water and windblown sand corrodes unprotected materials, and yes, even stainless steel. Our system utilizes a high strength carbon fiber material that is corrosion proof from salt water and UV proof. The system will not erode, decay or loose strength over time. The system has three installation conditions, for raising a house on existing pilings, repairing damaged pilings, and for connecting new pilings to floor joists in new construction. The three options are generally described here.</p>
  </div>

  <aside>
    <h3 class="abs services-head" style="font-weight:400">Our Services</h3>
    <div class="abs services-photo" role="img" aria-label="Photo of a hand in a suit holding a small model house beside a satisfaction guarantee plate"></div>
    <p class="abs services-text">The system will not erode, decay or loose strength over time. The system has three installation conditions, for raising a house on existing pilings, repairing damaged pilings,</p>
    <a class="abs know-more">Know More...</a>
  </aside>
</main>

<footer>
  <svg class="abs footer-shape" width="1148" height="1200" viewBox="0 0 1148 1200" aria-hidden="true">
    <path d="M0 991 H936 Q1041 991 1041 1096 V1153 H0 Z" fill="#474a40"/>
    <rect x="76" y="989" width="860" height="5" fill="#c5d6a0"/>
  </svg>

  <div class="abs quick-links">
    <h4 class="footer-col-title" style="font-weight:400">Qucik Links</h4>
    <div class="footer-rule" style="margin-top:6px"></div>
    <ul><li>Why Us</li><li>Privacy Policy</li><li>News &amp; Events</li><li>Contact Us</li></ul>
  </div>

  <div class="abs testimonials">
    <h4 class="footer-col-title" style="font-weight:400">Testimonials</h4>
    <div class="footer-rule" style="margin-top:6px"></div>
    <blockquote>Loren text we provided two systems, a complete system, Pile Cap Extension Pylonets, and Pile Splice.<cite>Dana Reyes</cite>USA</blockquote>
  </div>

  <div class="abs contact">
    <h4 class="footer-col-title" style="font-weight:400">Contact Us</h4>
    <div class="footer-rule" style="margin-top:6px"></div>
    <div class="org">Resilient Base Technologies, LLC</div>
    <address>PO Box 40512,&nbsp; Maple Valley,<br>PA 18000-0451<br>(555) 014-2290<br>Email: sales@resilientbase.example</address>
  </div>

  <div class="abs copyright-band"></div>
  <p class="abs copyright">Copyright © 2013&nbsp; Resilient Base Technologies. LLC&nbsp;&nbsp; All rights reserved.</p>
</footer>

</body>
</html>
```